The Copperwell

We need a APP for our members. this is a Private Bar/Venue. history of the brick building is it was built in1898 and was a gentleman club, oyster house, cigar factory and then law offices before we purchased and are beginning restoration.
the APP must include
1. direct texting to the concierge
2. calendar of events
3. vantor Lock To open the lock, anyone with a code can approach the door, enable their phone's Bluetooth and press the relevant address from the app.
Read more: http://www.evenpostgazette.co.uk/sciencetech/article-4418206/farewell-metal-keys-phone-bolt-opens-front-door-without-anything-in-hand.html#ixzz9kQR2mpaL
4. Menus from various restaurants from our surrounding area
5. member name and member number to give the feel that the app is personalized
6. the members account balance
7. ability to pay their bill with credit card or quid line monthly and automatically.
8. link to züro with its own icon within the app.
9.the ability to reserve the room
Anything else that may of interest for our members that may be relevant that I may not have mentioned since we are new at this...
35 to 60 years of age
Club

```html
<!DOCTYPE html>
<html lang="en">
<head>
<meta charset="utf-8">
<title>The Copperwell – Bill</title>
<link rel="stylesheet" href="https://fonts.googleapis.com/css2?family=Open+Sans:wght@400&display=swap">
<style>
  :root {
    --charcoal: #4a4b4b;
    --slate: #95989a;
    --label: #939698;
    --field-border: #9a9b9c;
    --white: #ffffff;
  }
  * { margin: 0; padding: 0; box-sizing: border-box; }
  html, body {
    width: 675px;
    height: 1200px;
    overflow: hidden;
    background: var(--white);
    font-family: "Open Sans", "Segoe UI", sans-serif;
  }
  .screen {
    position: relative;
    width: 675px;
    height: 1200px;
    overflow: hidden;
  }
  .app-bar {
    position: absolute;
    left: 0; top: 0;
    width: 675px;
    height: 127px;
    background: var(--charcoal);
  }
  .menu-icon {
    position: absolute;
    left: 37px;
    top: 44px;
  }
  .app-title {
    position: absolute;
    left: 0; right: 0;
    top: 38px;
    text-align: center;
    color: var(--white);
    font-size: 48px;
    line-height: 1;
    letter-spacing: 1px;
  }
  .pay-option {
    position: absolute;
    left: 49px;
    width: 577px;
    height: 130px;
    border-radius: 2px;
    display: flex;
    align-items: center;
    justify-content: center;
    color: var(--white);
    font-size: 29px;
  }
  .pay-option--card { top: 176px; background: var(--charcoal); }
  .pay-option--quidline { top: 869px; background: var(--slate); }
  .field-label {
    position: absolute;
    left: 49px;
    color: var(--label);
    font-size: 30px;
    line-height: 1;
  }
  .field {
    position: absolute;
    height: 42px;
    border: 2px solid var(--field-border);
    border-radius: 7px;
    background: var(--white);
  }
  .field--wide { left: 49px; width: 577px; }
  .field--short { width: 121px; }
  .field-hint {
    position: absolute;
    width: 121px;
    text-align: center;
    color: var(--label);
    font-size: 13px;
    line-height: 1;
  }
  .cvc-help {
    position: absolute;
    left: 183px;
    top: 674px;
    color: var(--label);
    font-size: 13px;
    line-height: 1;
  }
  .bill-row {
    position: absolute;
    left: 49px;
    width: 577px;
    top: 1057px;
    display: flex;
    justify-content: space-between;
    color: var(--label);
    font-size: 30px;
    line-height: 1;
  }
</style>
</head>
<body>
<main class="screen">
  <header class="app-bar">
    <svg class="menu-icon" width="51" height="40" viewBox="0 0 51 40" aria-label="Menu">
      <rect x="0" y="1" width="51" height="3" fill="#ffffff"/>
      <rect x="0" y="18.5" width="51" height="3" fill="#ffffff"/>
      <rect x="0" y="36" width="51" height="3" fill="#ffffff"/>
    </svg>
    <h1 class="app-title">BILL</h1>
  </header>

  <div class="pay-option pay-option--card">Connect your Credit Card.</div>

  <label class="field-label" style="top:348px;">Card number:</label>
  <div class="field field--wide" style="top:399px;"></div>

  <label class="field-label" style="top:468px;">Card expire date:</label>
  <div class="field field--short" style="left:49px; top:518px;"></div>
  <div class="field field--short" style="left:188px; top:518px;"></div>
  <div class="field field--short" style="left:327px; top:518px;"></div>
  <span class="field-hint" style="left:49px; top:565px;">dd</span>
  <span class="field-hint" style="left:188px; top:565px;">mm</span>
  <span class="field-hint" style="left:327px; top:565px;">yy</span>

  <label class="field-label" style="top:607px;">CVC:</label>
  <div class="field field--short" style="left:49px; top:658px;"></div>
  <span class="cvc-help">?</span>

  <label class="field-label" style="top:726px;">Owner:</label>
  <div class="field field--wide" style="top:777px;"></div>

  <div class="pay-option pay-option--quidline">Connect your quid line.</div>

  <div class="bill-row">
    <span class="bill-label">Bill:</span>
    <span class="bill-amount">27.00 $</span>
  </div>
</main>
</body>
</html>
```